Minimalist Planner/Journal Design

We need a planner/journal designed for daily use in a small group. I've attached a requirements document that outlines what every page needs to have on it. I've also attached a basic rough draft that we had made in Canva but the draft needs to be redesigned to look more in line with the style we need. I've attached some sample pages from some planners we like the style of. Feel free to add your own creativity and stylistic choices but keep in mind we are trying to get a very 'clean and minimalist design'. The deliverables should be both a pdf of the 8 planner pages, as well as the photoshop/gimp/illustrator files for the project.

Font styles to use
Other font styles liked:
• You choose, but we prefer thin , basic/minimal font faces

Requirements
Must have
• Minimal Design

```html
<!DOCTYPE html>
<html lang="en">
<head>
<meta charset="utf-8">
<title>Minimal Planner Pages</title>
<link rel="stylesheet" href="https://fonts.googleapis.com/css2?family=Amatic+SC:wght@400&display=swap">
<style>
  :root {
    --backdrop: #e7e8e9;
    --paper: #ffffff;
    --band: #fdfbdc;
    --band-strong: #fcf6c4;
    --dot-yellow: #fbeeaa;
    --ink: #c98a55;
    --rule: #dcb08c;
    --rule-soft: #ead2bd;
  }
  * { box-sizing: border-box; margin: 0; padding: 0; }
  html, body { width: 1200px; height: 720px; overflow: hidden; }
  body {
    background: var(--backdrop);
    font-family: "Amatic SC", "Arial Narrow", sans-serif;
    color: var(--ink);
    position: relative;
  }
  .page {
    position: absolute;
    width: 221px;
    height: 287px;
    background: var(--paper);
  }
  .page > * { position: absolute; }
  .label {
    font-size: 6.5px;
    line-height: 1;
    letter-spacing: 0.1px;
    white-space: nowrap;
    text-transform: uppercase;
  }
  .title-band {
    left: 17px; top: 15px;
    width: 89px; height: 7px;
    background: var(--band);
    padding-left: 2px;
    font-size: 6.5px; line-height: 7px;
    text-transform: uppercase;
  }
  .dot-rows {
    background-image: radial-gradient(circle, var(--rule) 0.45px, transparent 0.65px);
    background-size: 2.6px var(--gap, 9px);
    background-position: 0 calc(var(--gap, 9px) - 1.3px);
  }
  .dot-line {
    height: 1px;
    background-image: radial-gradient(circle, var(--rule) 0.45px, transparent 0.65px);
    background-size: 2.6px 1px;
  }
  .answer-box { background: var(--band); }
  .check {
    display: inline-block;
    width: 4px; height: 4px;
    border: 0.5px solid var(--ink);
    vertical-align: middle;
    margin-left: 1px;
  }
  .day-label {
    left: 152px; width: 53px;
    border-bottom: 0.5px solid var(--rule);
    padding-bottom: 1px;
    font-size: 6.5px; line-height: 1;
    text-transform: uppercase;
  }
  .weekday-dot { text-align: center; font-size: 3.5px; line-height: 1; width: 8px; }
  .weekday-dot i {
    display: block; margin: 1px auto 0;
    width: 5px; height: 5px; border-radius: 50%;
    border: 0.5px solid var(--ink);
  }
  .schedule {
    left: 144px; top: 46px; width: 62px; height: 200px;
    background:
      linear-gradient(var(--band-strong), var(--band-strong)) 0 0 / 16px 100% no-repeat,
      repeating-linear-gradient(to bottom, var(--rule) 0 0.5px, transparent 0.5px 8.7px);
    border-bottom: 0.5px solid var(--rule);
  }
  .score-line { border-bottom: 0.5px solid var(--rule-soft); }
  .score-cells { display: flex; border: 0.5px solid var(--rule); border-top: none; height: 5px; }
  .score-cells span { flex: 1; border-right: 0.5px solid var(--rule); }
  .score-cells span:last-child { border-right: none; }
  .steps-table {
    left: 17px; top: 121px; width: 187px; height: 38px;
    background:
      linear-gradient(var(--band-strong), var(--band-strong)) 0 0 / 17px 100% no-repeat,
      repeating-linear-gradient(to bottom, transparent 0 9px, var(--rule) 9px 9.5px);
    border-top: 0.5px solid var(--rule);
  }
  .steps-table::after {
    content: ""; position: absolute; left: 17px; top: 0; bottom: 0;
    border-left: 0.5px solid var(--rule);
  }
  .habit-streak {
    left: 17px; top: 219px; width: 11px; height: 51px;
    background: var(--band-strong);
    border: 0.5px solid var(--rule);
  }
  .habit-streak span {
    position: absolute; left: 50%; top: 50%;
    transform: translate(-50%, -50%) rotate(-90deg);
    font-size: 5px; white-space: nowrap;
  }
</style>
</head>
<body>

<!-- Goals -->
<section class="page" style="left:108px; top:53px;">
  <div class="title-band">Goals</div>
  <div class="dot-rows" style="left:16px; top:28px; width:126px; height:45px; --gap:12.3px;"></div>
  <div class="label" style="left:16px; top:82px;">Health<span class="check"></span>&nbsp;&nbsp;&nbsp;&nbsp;&nbsp;&nbsp;Financial <span class="check"></span>&nbsp;&nbsp;&nbsp;&nbsp;&nbsp;&nbsp;Spiritual <span class="check"></span></div>
  <div class="label" style="left:16px; top:94px;">Career <span class="check"></span>&nbsp;&nbsp;&nbsp;&nbsp;&nbsp;&nbsp;Family/Relationship <span class="check"></span></div>
  <div class="title-band" style="left:16px; top:108px;">3 Weekly Goals</div>
  <div class="label" style="left:16px; top:119px;">1</div>
  <div class="dot-rows" style="left:16px; top:120px; width:126px; height:41px; --gap:10.2px;"></div>
  <div class="label" style="left:16px; top:174px;">2</div>
  <div class="dot-rows" style="left:16px; top:174px; width:126px; height:41px; --gap:10.2px;"></div>
  <div class="label" style="left:16px; top:227px;">3</div>
  <div class="dot-rows" style="left:16px; top:228px; width:126px; height:41px; --gap:10.2px;"></div>
  <div class="day-label" style="top:29px;">Monday</div>
  <div class="day-label" style="top:63px;">Tuesday</div>
  <div class="day-label" style="top:96px;">Wednesday</div>
  <div class="day-label" style="top:130px;">Thursday</div>
  <div class="day-label" style="top:163px;">Friday</div>
  <div class="day-label" style="top:197px;">Saturday</div>
  <div class="day-label" style="top:230px;">Sunday</div>
</section>

<!-- Week -->
<section class="page" style="left:362px; top:53px;">
  <div class="title-band">Week</div>
  <div class="weekday-dot" style="left:129px; top:15px;">Mon<i></i></div>
  <div class="weekday-dot" style="left:141px; top:15px;">Tue<i></i></div>
  <div class="weekday-dot" style="left:153px; top:15px;">Wed<i></i></div>
  <div class="weekday-dot" style="left:165px; top:15px;">Thu<i></i></div>
  <div class="weekday-dot" style="left:177px; top:15px;">Fri<i></i></div>
  <div class="weekday-dot" style="left:189px; top:15px;">Sat<i></i></div>
  <div class="weekday-dot" style="left:201px; top:15px;">Sun<i></i></div>
  <div class="label" style="left:18px; top:31px;">Primary Task</div>
  <div class="label" style="left:18px; top:44px;"><span class="check"></span> 1</div>
  <div class="dot-rows" style="left:30px; top:39px; width:99px; height:36px; --gap:8.8px;"></div>
  <div class="label" style="left:18px; top:86px;"><span class="check"></span> 2</div>
  <div class="dot-rows" style="left:30px; top:81px; width:99px; height:36px; --gap:8.8px;"></div>
  <div class="label" style="left:18px; top:127px;"><span class="check"></span> 3</div>
  <div class="dot-rows" style="left:30px; top:122px; width:99px; height:36px; --gap:8.8px;"></div>
  <div class="label" style="left:18px; top:170px;">Secondary Task</div>
  <div class="dot-rows" style="left:17px; top:178px; width:112px; height:62px; --gap:8.8px;"></div>
  <div class="label" style="left:18px; top:246px;"><span class="check"></span> Physical Activity</div>
  <div class="label" style="left:18px; top:254px;"><span class="check"></span> Habit</div>
  <div class="label" style="left:18px; top:263px;"><span class="check"></span> Weekly Challenge</div>
  <div class="schedule"></div>
  <div class="label" style="left:148px; top:49px; font-size:5px;">5 AM</div>
  <div class="label" style="left:142px; top:263px;">Daily Score W/L</div>
  <div class="score-line" style="left:173px; top:268px; width:32px;"></div>
</section>

<!-- Notes -->
<section class="page" style="left:617px; top:53px;">
  <div class="title-band">Notes</div>
  <div class="dot-rows" style="left:17px; top:25px; width:187px; height:244px; --gap:9px;"></div>
</section>

<!-- Weekly Review -->
<section class="page" style="left:872px; top:53px;">
  <div class="title-band">Weekly Review</div>
  <div class="label" style="left:17px; top:31px;">What did I learn this week/ what can I take away?</div>
  <div class="answer-box" style="left:17px; top:41px; width:187px; height:33px;"></div>
  <div class="label" style="left:17px; top:80px;">Did I execute what I needed to move forward in my goals?</div>
  <div class="answer-box" style="left:17px; top:89px; width:187px; height:33px;"></div>
  <div class="label" style="left:17px; top:128px;">What can I improve/keep doing for next week?</div>
  <div class="answer-box" style="left:17px; top:136px; width:187px; height:34px;"></div>
  <div class="title-band" style="left:17px; top:177px;">Notes</div>
  <div class="dot-rows" style="left:17px; top:182px; width:187px; height:74px; --gap:9.2px;"></div>
  <div class="label" style="left:17px; top:264px; font-size:4px;">Daily Score</div>
  <div class="score-cells" style="left:35px; top:264px; width:63px;"><span></span><span></span><span></span><span></span><span></span><span></span><span></span></div>
  <div class="label" style="left:163px; top:264px; font-size:4px;">Weekly W/L</div>
  <div class="score-cells" style="left:183px; top:264px; width:21px;"><span></span></div>
</section>

<!-- Month -->
<section class="page" style="left:108px; top:369px;">
  <div class="title-band">Month</div>
  <svg style="left:16px; top:29px;" width="189" height="151" viewBox="0 0 189 151" aria-hidden="true">
    <g fill="var(--dot-yellow)">
      <circle cx="4" cy="4" r="3"/><circle cx="31" cy="4" r="3"/><circle cx="58" cy="4" r="3"/><circle cx="85" cy="4" r="3"/><circle cx="112" cy="4" r="3"/><circle cx="139" cy="4" r="3"/><circle cx="166" cy="4" r="3"/>
      <circle cx="4" cy="29" r="3"/><circle cx="31" cy="29" r="3"/><circle cx="58" cy="29" r="3"/><circle cx="85" cy="29" r="3"/><circle cx="112" cy="29" r="3"/><circle cx="139" cy="29" r="3"/><circle cx="166" cy="29" r="3"/>
      <circle cx="4" cy="54" r="3"/><circle cx="31" cy="54" r="3"/><circle cx="58" cy="54" r="3"/><circle cx="85" cy="54" r="3"/><circle cx="112" cy="54" r="3"/><circle cx="139" cy="54" r="3"/><circle cx="166" cy="54" r="3"/>
      <circle cx="4" cy="79" r="3"/><circle cx="31" cy="79" r="3"/><circle cx="58" cy="79" r="3"/><circle cx="85" cy="79" r="3"/><circle cx="112" cy="79" r="3"/><circle cx="139" cy="79" r="3"/><circle cx="166" cy="79" r="3"/>
      <circle cx="4" cy="104" r="3"/><circle cx="31" cy="104" r="3"/><circle cx="58" cy="104" r="3"/><circle cx="85" cy="104" r="3"/><circle cx="112" cy="104" r="3"/><circle cx="139" cy="104" r="3"/><circle cx="166" cy="104" r="3"/>
      <circle cx="4" cy="129" r="3"/><circle cx="31" cy="129" r="3"/><circle cx="58" cy="129" r="3"/><circle cx="85" cy="129" r="3"/><circle cx="112" cy="129" r="3"/><circle cx="139" cy="129" r="3"/><circle cx="166" cy="129" r="3"/>
    </g>
    <g stroke="var(--rule-soft)" stroke-width="0.5" fill="none">
      <rect x="0.5" y="0.5" width="188" height="150"/>
      <path d="M27.4 0.5V150.5M54.3 0.5V150.5M81.1 0.5V150.5M108 0.5V150.5M134.9 0.5V150.5M161.7 0.5V150.5"/>
      <path d="M0.5 25.5H188.5M0.5 50.5H188.5M0.5 75.5H188.5M0.5 100.5H188.5M0.5 125.5H188.5"/>
    </g>
  </svg>
  <div class="title-band" style="left:17px; top:190px;">Notes</div>
  <div class="dot-rows" style="left:16px; top:198px; width:189px; height:72px; --gap:9px;"></div>
</section>

<!-- Weekly Overview -->
<section class="page" style="left:362px; top:369px;">
  <div class="title-band">Weekly Overview</div>
  <div class="dot-rows" style="left:17px; top:22px; width:187px; height:27px; --gap:8.7px;"></div>
  <div class="label" style="left:17px; top:55px; font-size:6px;">Health<span class="check"></span>&nbsp;&nbsp;&nbsp; Career<span class="check"></span>&nbsp;&nbsp;&nbsp; Intellectual<span class="check"></span>&nbsp;&nbsp;&nbsp; Spiritual<span class="check"></span>&nbsp;&nbsp;&nbsp; Relationship/Family<span class="check"></span>&nbsp;&nbsp;&nbsp; Finacial<span class="check"></span></div>
  <div class="label" style="left:17px; top:66px;">How will you measure success?</div>
  <div class="answer-box" style="left:17px; top:75px; width:187px; height:34px;"></div>
  <div class="label" style="left:17px; top:113px;">What are the first actionable steps you can take?</div>
  <div class="steps-table"></div>
  <div class="label" style="left:17px; top:164px;">Why do you want to achieve this?</div>
  <div class="answer-box" style="left:17px; top:172px; width:187px; height:34px;"></div>
  <div class="habit-streak"><span>Habit Streak</span></div>
  <div class="label" style="left:53px; top:212px; transform:translateX(-50%);">Month 1</div>
  <div class="label" style="left:112px; top:212px; transform:translateX(-50%);">Month 2</div>
  <div class="label" style="left:170px; top:212px; transform:translateX(-50%);">Month 3</div>
  <svg style="left:35px; top:219px;" width="170" height="52" viewBox="0 0 170 52" aria-hidden="true">
    <defs>
      <pattern id="streak-cell" width="7.43" height="8.5" patternUnits="userSpaceOnUse">
        <path d="M7.43 0V8.5M0 8.5H7.43" stroke="var(--rule-soft)" stroke-width="0.5" fill="none"/>
      </pattern>
    </defs>
    <g stroke="var(--rule-soft)" stroke-width="0.5">
      <rect x="0.25" y="0.25" width="52" height="51" fill="url(#streak-cell)"/>
      <rect x="60.25" y="0.25" width="52" height="51" fill="url(#streak-cell)"/>
      <rect x="117.75" y="0.25" width="52" height="51" fill="url(#streak-cell)"/>
    </g>
  </svg>
</section>

<!-- Review Goals: week -->
<section class="page" style="left:617px; top:369px;">
  <div class="title-band">Review Goals</div>
  <div class="label" style="left:17px; top:34px;">Did I execute what I needed to in order to move forward in my progress?</div>
  <div class="answer-box" style="left:17px; top:42px; width:187px; height:58px;"></div>
  <div class="label" style="left:18px; top:111px;">What can I take away from this week/ lessons learned?</div>
  <div class="answer-box" style="left:17px; top:119px; width:187px; height:58px;"></div>
  <div class="title-band" style="left:17px; top:190px;">Notes</div>
  <div class="dot-rows" style="left:17px; top:198px; width:187px; height:72px; --gap:9px;"></div>
</section>

<!-- Review Goals: quarter -->
<section class="page" style="left:872px; top:369px;">
  <div class="title-band">Review Goals</div>
  <div class="label" style="left:17px; top:34px;">Did I have a meaningful impact on my life this quarter?</div>
  <div class="answer-box" style="left:17px; top:42px; width:187px; height:58px;"></div>
  <div class="label" style="left:18px; top:111px;">Did I meet my goals? Why or why not?</div>
  <div class="answer-box" style="left:17px; top:119px; width:187px; height:58px;"></div>
  <div class="title-band" style="left:17px; top:190px;">Notes</div>
  <div class="dot-rows" style="left:17px; top:198px; width:187px; height:72px; --gap:9px;"></div>
</section>

</body>
</html>
```